Home page graphic design only (NOT WEBSITE DESIGN)

I require a home page to be designed for my new website.
I DO NOT REQUIRE to build a website. We are a rug company specialising in alpaca wool. It is targeted at the high end of the market and hence the graphics of our page requires to reflect this. Our current page is as per attachment and I think it is too basic.
Updates

Target Market(s)

Extremly high net worth individuals where luxury is a requirement

Requirements
Must have
• show of style, luxury, uniqueness. Prefer having bright images.
Nice to have
• a highly sofisticated roomscape where the focus in the rug. See attachment as an example
Should not have
• Not sure

```html
<!DOCTYPE html>
<html lang="en">
<head>
<meta charset="utf-8">
<title>Maison Laine – Home</title>
<link rel="stylesheet" href="https://fonts.googleapis.com/css2?family=Cormorant+Garamond:wght@500&family=Inter:wght@300;400;600;700&display=swap">
<style>
  :root {
    --gold: #f2bb3f;
    --gold-soft: rgba(243, 208, 110, 0.62);
    --gold-pale: #f8e6b2;
    --ink: #2b2b2b;
    --nav-ink: #444;
    --bar: #f2f2f2;
    --active: #c9c9c9;
    --corner-dark: #2a2a2a;
  }
  * { margin: 0; padding: 0; box-sizing: border-box; }
  html, body { width: 1200px; height: 702px; overflow: hidden; background: var(--bar); }
  body { font-family: "Inter", sans-serif; color: var(--ink); position: relative; }

  .site-header { position: absolute; left: 0; top: 0; width: 1200px; height: 82px; background: var(--bar); }
  .brand-name { position: absolute; left: 35px; top: 14px; font-family: "Cormorant Garamond", serif; font-weight: 500; font-size: 46px; letter-spacing: 1px; color: var(--gold); line-height: 1; }
  .main-nav a { position: absolute; top: 0; height: 82px; line-height: 90px; font-size: 14px; font-weight: 300; color: var(--nav-ink); text-decoration: none; white-space: nowrap; }
  .main-nav a.is-active { background: var(--active); font-weight: 600; color: #333; text-align: center; }
  .nav-chevron { display: inline-block; margin-left: 6px; vertical-align: middle; }
  .brand-tile { position: absolute; left: 1127px; top: 0; width: 73px; height: 82px; background: var(--gold); display: flex; flex-direction: column; align-items: center; justify-content: center; gap: 4px; }
  .brand-tile .dot { width: 18px; height: 18px; border-radius: 50%; background: var(--ink); }
  .brand-tile span { font-size: 8px; font-weight: 600; color: var(--ink); letter-spacing: .5px; }

  .hero { position: absolute; left: 0; top: 82px; width: 1200px; height: 590px; overflow: hidden; }
  .hero-scene { position: absolute; inset: 0; background: linear-gradient(180deg, #f4f3f1 0%, #efeeec 45%, #e7e4e0 72%, #eee6da 100%); }
  .hero-tint { position: absolute; left: 734px; top: 0; width: 389px; height: 590px; background: var(--gold-soft); }
  .hero-tint-edge { position: absolute; left: 1123px; top: 0; width: 77px; height: 590px; background: var(--gold-pale); opacity: .8; }

  .feature-frame { position: absolute; }
  .corner-gold { left: 640px; top: 94px; width: 48px; height: 47px; background: var(--gold); position: absolute; }
  .corner-dark { left: 1079px; top: 403px; width: 47px; height: 47px; background: var(--corner-dark); position: absolute; }
  .feature-photo { position: absolute; left: 650px; top: 105px; width: 466px; height: 334px; background: linear-gradient(160deg, #eef1ee 0%, #a9cbbf 30%, #e8b447 55%, #d8cfc2 75%, #bdb5ad 100%); }

  .hero-copy { position: absolute; left: 74px; top: 176px; }
  .hero-lead { font-size: 35px; font-weight: 300; line-height: 43px; letter-spacing: .3px; color: var(--ink); }
  .hero-title { font-size: 59px; font-weight: 700; line-height: 70px; letter-spacing: -.5px; color: var(--ink); margin-top: 3px; }

  .hero-meta { position: absolute; left: 74px; top: 510px; }
  .est-badge { display: inline-block; background: var(--gold); font-size: 12px; padding: 2px 6px; color: var(--ink); }
  .markets { font-size: 15px; font-weight: 300; margin-top: 3px; color: var(--ink); }
  .company { font-size: 8.5px; font-weight: 700; margin-top: 3px; }

  .site-footer { position: absolute; left: 0; top: 672px; width: 1200px; height: 30px; background: var(--bar); font-size: 9px; color: var(--ink); }
  .social { position: absolute; left: 17px; top: 8px; display: flex; gap: 7px; }
  .social i { width: 14px; height: 14px; border-radius: 50%; background: var(--ink); display: block; }
  .address { position: absolute; left: 86px; top: 9px; letter-spacing: .2px; }
  .copyright { position: absolute; right: 23px; top: 9px; }
</style>
</head>
<body>
  <header class="site-header">
    <div class="brand-name">Maison Laine</div>
    <nav class="main-nav">
      <a style="left:364px">Home</a>
      <a class="is-active" style="left:415px;width:102px">Collections</a>
      <a style="left:530px">Our Story<svg class="nav-chevron" width="10" height="7" viewBox="0 0 10 7"><path d="M1 1l4 4 4-4" fill="none" stroke="#444" stroke-width="1.6"/></svg></a>
      <a style="left:634px">About Us</a>
      <a style="left:719px">Publications</a>
      <a style="left:828px">News &amp; Events</a>
      <a style="left:952px">Contact Us</a>
      <a style="left:1055px">FAQ</a>
    </nav>
    <div class="brand-tile"><div class="dot"></div><span>Maison Laine</span></div>
  </header>

  <section class="hero">
    <div class="hero-scene" role="img" aria-label="Bright living room with white sofa, marble tables and a pale striped alpaca rug by a sea view window"></div>
    <div class="hero-tint"></div>
    <div class="hero-tint-edge"></div>

    <div class="corner-gold"></div>
    <div class="corner-dark"></div>
    <div class="feature-photo" role="img" aria-label="Room with a mustard velvet loveseat, mint wall, bookshelf and a geometric pastel alpaca rug on a timber floor"></div>

    <div class="hero-copy">
      <p class="hero-lead">Exquisite luxury carpeting<br>and area rugs made from pure</p>
      <h1 class="hero-title">Premium Alpaca</h1>
    </div>

    <div class="hero-meta">
      <span class="est-badge">Estabilished in 1988</span>
      <p class="markets">Australia | USA | Europe | UK | Asia | UAE</p>
      <p class="company">Maison Laine Pty Ltd</p>
    </div>
  </section>

  <footer class="site-footer">
    <div class="social"><i></i><i></i><i></i></div>
    <p class="address">Australia | Head Office : Suite 8 / Unit 112 - 54 Willow Vale Road, Fernbrook VIC 3125</p>
    <p class="copyright">Copyright 2020©</p>
  </footer>
</body>
</html>
```